women's junior contemporary apparel company.
We are looking for a business card that represents our urban design aesthetic. We would like to keep it simple and modern/contemporary.
the name of the company is 'v-lanza'.

we've attached a font style but you are not limited solely to use this font. All suggestions are welcomed.

```html
<!DOCTYPE html>
<html lang="en">
<head>
<meta charset="utf-8">
<title>v-lanza business card</title>
<link href="https://fonts.googleapis.com/css2?family=Archivo:wght@800&display=swap" rel="stylesheet">
<style>
  :root {
    --page: #ecebe8;
    --card-grey: #a6a6a6;
    --panel-white: #ffffff;
    --ink: #111111;
    --photo-light: #e6e6ea;
    --frame: #8a8a8a;
  }
  * { box-sizing: border-box; margin: 0; padding: 0; }
  html, body { width: 1100px; height: 1200px; overflow: hidden; }
  body {
    background: var(--page);
    display: flex;
    flex-direction: column;
    align-items: center;
    justify-content: center;
    gap: 60px;
  }
  .card {
    width: 900px;
    height: 500px;
    background: var(--card-grey);
    position: relative;
    box-shadow: 0 6px 18px rgba(0,0,0,0.18);
  }
  .wordmark {
    font-family: "Archivo", "Arial Black", sans-serif;
    font-weight: 800;
    color: var(--ink);
    line-height: 1;
    letter-spacing: 1px;
    white-space: nowrap;
  }
  /* Front */
  .front-panel {
    position: absolute;
    left: 54px; right: 54px; top: 44px; bottom: 50px;
    background: var(--panel-white);
    border: 2px solid var(--frame);
    display: flex;
    flex-direction: column;
  }
  .front-header {
    height: 88px;
    display: flex;
    align-items: center;
    justify-content: center;
  }
  .front-header .wordmark { font-size: 58px; }
  .photo-grid {
    flex: 1;
    display: grid;
    grid-template-columns: 40% 23% 1fr;
    grid-template-rows: 34% 1fr;
    gap: 6px;
    padding: 0 4px 4px;
  }
  .photo { border: 2px solid var(--frame); }
  .photo-tall-left {
    grid-row: 1 / 3;
    background: linear-gradient(160deg, #d8d4cf 0%, #b59a86 35%, #3f6f77 60%, #2a2d3a 100%);
  }
  .photo-mid-top {
    background: linear-gradient(135deg, #9c9a98 0%, #d8b6a3 55%, #cfcac6 100%);
  }
  .photo-mid-bottom {
    background: linear-gradient(160deg, #ededed 0%, #c9b28f 35%, #2b2e2c 70%, #5c6a48 100%);
  }
  .photo-tall-right {
    grid-row: 1 / 3;
    grid-column: 3;
    background: linear-gradient(165deg, #8a8f95 0%, #b8a79a 30%, #7d98b8 60%, #a6bcd2 100%);
  }
  /* Back */
  .back-photo {
    position: absolute;
    left: 0; right: 0; top: 0;
    height: 290px;
    background: linear-gradient(90deg, var(--photo-light) 0%, #dcd9db 40%, #8c6a52 50%, #dcd9db 60%, var(--photo-light) 100%);
  }
  .back-band {
    position: absolute;
    left: 0; right: 0; top: 290px; bottom: 0;
    display: flex;
    align-items: center;
    justify-content: space-between;
    padding: 0 50px 0 92px;
  }
  .contact-list { list-style: none; }
  .contact-item {
    display: flex;
    align-items: center;
    gap: 14px;
    font-family: "Archivo", "Arial Black", sans-serif;
    font-weight: 800;
    font-size: 21px;
    letter-spacing: 1.5px;
    color: var(--ink);
    line-height: 34px;
    text-transform: uppercase;
    white-space: nowrap;
  }
  .contact-icon { width: 16px; height: 16px; flex: none; }
  .back-band .wordmark { font-size: 50px; margin-top: 10px; }
</style>
</head>
<body>
  <section class="card card-front">
    <div class="front-panel">
      <header class="front-header"><span class="wordmark">v-lanza</span></header>
      <div class="photo-grid">
        <div class="photo photo-tall-left" role="img" aria-label="Street-style photo of a person in a patterned bomber jacket and jeans"></div>
        <div class="photo photo-mid-top" role="img" aria-label="Photo of a back with criss-cross top straps"></div>
        <div class="photo photo-mid-bottom" role="img" aria-label="Photo of a model in a printed jacket and crop top"></div>
        <div class="photo photo-tall-right" role="img" aria-label="Street-style photo of a woman in a denim coat and ripped jeans"></div>
      </div>
    </div>
  </section>

  <section class="card card-back">
    <div class="back-photo" role="img" aria-label="Portrait photo of a model in a grey t-shirt on a pale backdrop"></div>
    <div class="back-band">
      <ul class="contact-list">
        <li class="contact-item">
          <svg class="contact-icon" viewBox="0 0 16 16"><path d="M8 1a5 5 0 0 0-5 5c0 3.8 5 9 5 9s5-5.2 5-9a5 5 0 0 0-5-5zm0 7a2 2 0 1 1 0-4 2 2 0 0 1 0 4z" fill="#111"/></svg>
          Your Address
        </li>
        <li class="contact-item">
          <svg class="contact-icon" viewBox="0 0 16 16"><rect x="1" y="3" width="14" height="10" fill="#111"/><path d="M1.5 3.5 8 9l6.5-5.5" stroke="#a6a6a6" stroke-width="1.3" fill="none"/></svg>
          Your Email.com
        </li>
        <li class="contact-item">
          <svg class="contact-icon" viewBox="0 0 16 16"><path d="M1 5c0-2 3-3 7-3s7 1 7 3v1h-3.5V4.5h-7V6H1zM3 8h10l1 6H2z" fill="#111"/><circle cx="8" cy="11" r="1.6" fill="#a6a6a6"/></svg>
          Your Phone Number
        </li>
        <li class="contact-item">
          <svg class="contact-icon" viewBox="0 0 16 16" fill="none" stroke="#111" stroke-width="1.4"><circle cx="8" cy="8" r="6.5"/><ellipse cx="8" cy="8" rx="2.8" ry="6.5"/><path d="M1.5 8h13M2.5 4.8h11M2.5 11.2h11"/></svg>
          www.northlanestudio.com
        </li>
      </ul>
      <span class="wordmark">v-lanza</span>
    </div>
  </section>
</body>
</html>
```